Willow Glow & Laser - Business Banner with Brand Elements

Design:
• We would like to get a creative design for a wide banner that will go outside our medical spa clinic location. We need a designer to make a simple yet colorful and high-quality design layout. We want this banner to be eye-catching and to communicate the services we offer at our business: Laser Hair Removal | Velonix | Lip Filler.

Requirements:
• We would like the banner to include our companies information which is the following:

Logo
“Refresh Your Skin”
Laser Hair Removal | Velonix | Lip Filler
(555) 287-1936
www.WillowGlowLaser.com

Colors:
• Our business colors are orange, a hint of black and white, but mostly peach/orange tones. (Orange: #f78f20 , White: #ffffff)

Fonts:
• Josefins Sans Bold & Lato

Content and images can be located here:
https://files.cloudvaultshare.com/folders/7tQmZ2xVbR9kLpN4sW8yH3cD6fJ1gA0eU?usp=sharing

The following will give you an idea of our brand presentation:
• Our website is: www.WillowGlowLaser.com
• Our Instagram; @willowglowlaser
• Our Facebook: www.socialpagehub.com/willowglowlaser

Target Market(s)
• Women 25 - 45

Industry/Entity Type
• Beauty

```html
<!DOCTYPE html>
<html lang="en">
<head>
<meta charset="utf-8">
<title>Willow Glow &amp; Laser – Banner Options</title>
<link href="https://fonts.googleapis.com/css2?family=Josefin+Sans:wght@700&family=Lato:wght@400;700;900&display=swap" rel="stylesheet">
<style>
  :root {
    --stage: #262626;
    --orange: #f78f20;
    --panel-orange: #fba43e;
    --ink: #151515;
    --white: #ffffff;
    --peach-light: #fdd6a3;
    --peach-mid: #f8bd7d;
    --photo-light: #ffffff;
    --photo-soft: #f1ece6;
  }
  * { margin: 0; padding: 0; box-sizing: border-box; }
  html, body { width: 1179px; height: 1200px; overflow: hidden; }
  body { background: var(--stage); position: relative; }

  .banner {
    position: absolute; left: 112px; width: 956px; height: 362px;
    display: flex; box-shadow: 0 8px 24px rgba(0,0,0,.35);
  }
  .banner--orange { top: 177px; }
  .banner--dark { top: 629px; }

  .banner__photo { width: 475px; height: 100%; }
  .banner--orange .banner__photo { background: radial-gradient(ellipse at 55% 45%, var(--peach-light), var(--peach-mid)); }
  .banner--dark .banner__photo { background: radial-gradient(ellipse at 55% 50%, var(--photo-soft), var(--photo-light)); }

  .banner__divider { width: 8px; height: 100%; }
  .banner--orange .banner__divider { background: var(--ink); }
  .banner--dark .banner__divider { background: var(--orange); }

  .banner__panel { position: relative; flex: 1; height: 100%; }
  .banner--orange .banner__panel { background: var(--panel-orange); }
  .banner--dark .banner__panel { background: var(--ink); }

  .brand {
    position: absolute; right: 16px; top: 10px;
    display: flex; align-items: center; gap: 6px;
    font-family: "Josefin Sans", sans-serif; font-weight: 700;
    font-size: 15px; line-height: 24px; color: var(--ink);
  }
  .brand__dot { width: 22px; height: 22px; border-radius: 50%; background: var(--white); flex: none; }
  .banner--dark .brand { color: var(--white); }
  .banner--dark .brand__dot { background: var(--orange); }

  .headline {
    position: absolute; left: 27px; top: 38px;
    font-family: "Josefin Sans", sans-serif; font-weight: 700;
    font-size: 50px; line-height: 56px; letter-spacing: 1px;
    color: var(--ink); text-transform: uppercase;
  }
  .banner--dark .headline { color: var(--orange); }

  .services {
    position: absolute; left: 25px; top: 148px; width: 289px; height: 75px;
    border: 1.5px solid var(--white); padding: 2px 8px;
    font-family: "Lato", sans-serif; font-weight: 900;
    font-size: 29px; line-height: 35px; color: var(--white);
  }

  .contact-row { position: absolute; left: 0; top: 260px; width: 420px; height: 34px; }
  .contact-row svg { position: absolute; inset: 0; }
  .contact-row__label {
    position: absolute; left: 25px; top: 7px;
    font-family: "Josefin Sans", sans-serif; font-weight: 700; font-size: 21px;
    color: var(--white);
  }
  .banner--dark .contact-row__label { color: var(--ink); }
  .contact-row__phone {
    position: absolute; left: 152px; top: 1px;
    font-family: "Josefin Sans", sans-serif; font-weight: 700; font-size: 35px;
    color: var(--orange); letter-spacing: .5px;
  }
  .banner--dark .contact-row__phone { color: var(--ink); }

  .website {
    position: absolute; left: 26px; top: 311px;
    font-family: "Lato", sans-serif; font-weight: 400; font-size: 29px;
    color: var(--white); letter-spacing: -.3px;
  }
</style>
</head>
<body>

  <section class="banner banner--orange">
    <div class="banner__photo" role="img" aria-label="Portrait of three women with glowing skin on a peach backdrop"></div>
    <div class="banner__divider"></div>
    <div class="banner__panel">
      <div class="brand"><span class="brand__dot"></span>Willow Glow &amp; Laser</div>
      <h1 class="headline">Refresh<br>Your Skin</h1>
      <p class="services">Laser Hair Removal<br>| Velonix | Lip Filler</p>
      <div class="contact-row">
        <svg width="420" height="34" viewBox="0 0 420 34">
          <polygon points="0,0 128,0 117,34 0,34" fill="#151515"/>
          <polygon points="139,0 418,0 406,34 127,34" fill="#ffffff"/>
        </svg>
        <span class="contact-row__label">PHONE</span>
        <span class="contact-row__phone">(555) 287-1936</span>
      </div>
      <p class="website">www.WillowGlowLaser.com</p>
    </div>
  </section>

  <section class="banner banner--dark">
    <div class="banner__photo" role="img" aria-label="Portrait of three women with glowing skin on a white backdrop"></div>
    <div class="banner__divider"></div>
    <div class="banner__panel">
      <div class="brand"><span class="brand__dot"></span>Willow Glow &amp; Laser</div>
      <h1 class="headline">Refresh<br>Your Skin</h1>
      <p class="services">Laser Hair Removal<br>| Velonix | Lip Filler</p>
      <div class="contact-row">
        <svg width="420" height="34" viewBox="0 0 420 34">
          <polygon points="0,0 128,0 117,34 0,34" fill="#fba43e"/>
          <polygon points="139,0 418,0 406,34 127,34" fill="#ffffff"/>
        </svg>
        <span class="contact-row__label">PHONE</span>
        <span class="contact-row__phone">(555) 287-1936</span>
      </div>
      <p class="website">www.WillowGlowLaser.com</p>
    </div>
  </section>

</body>
</html>
```